Re-Design Of High Traffic Content Hub

“Tarmac Compass, is a comprehensive online hub dedicated to helping over 150,000 visitors a month have a smooth towing trip. Tarmac Compass is the place where you’ll find up-to-date information, practical advice, ‘how to’ guides and handy tips for your caravan, trailer and anything else you need to tow."

Content on the site is split in to 4 main pillars:
“Caravan” “Trailer” “Boating” "Travel"

Each pillar is split further in to 3 categories:
How To • Products • Reviews

We are crowd-sourcing the redesign of the following pages:

- Home Page
- Category Page
- Single Post
- Search Results
- Static Content Page (Terms & Conditions/ About / Privacy Policy)

Look and feel to be implemented inline with UX best practice.
A strong conversion focus is desirable site wide (e-book downloads & newsletter subscriptions are offered).

Our preference is for the home page to provide the visitor with a visual snapshot of fresh site content and encourage the user to explore the site further using navigation or search.

Design elements to be featured on the home page:
Main Navigation
Site Search
Newsletter Subscription Box
eBook Download CTA
Mission Statement
2 x Recent articles from each top level content pillar including featured image and title.
An area to feature 3 of the site's best performing articles including featured image, title and excerpt.

Mission Statement: "Tarmac Compass is the place you can turn to for up-to-date information, practical advice, ‘how to’ guides and handy tips for your caravan, trailer and anything else worth towing. "

Selected designs will be coded in responsive bootstrap so preference will be given to designs presented with this in mind.

Logo's attached in transparent white and transparent dark.

Live site located at www.tarmaccompass-demo.com.au

ec1f27
f5f5f5
b2b2b2
ffffff

• Strong conversion focus (eBook downloads and newsletter subscriptions)

```html
<!DOCTYPE html>
<html lang="en">
<head>
<meta charset="utf-8">
<title>Tarmac Compass — Home</title>
<link href="https://fonts.googleapis.com/css2?family=Oswald:wght@400;500&family=Raleway:ital,wght@0,400;0,600;0,700;1,400&display=swap" rel="stylesheet">
<style>
:root{
  --red:#ec1f27;
  --light:#f5f5f5;
  --grey:#b2b2b2;
  --white:#ffffff;
  --ink:#333333;
  --muted:#8a8a8a;
  --shadow:#dcdcdc;
}
*{box-sizing:border-box;margin:0;padding:0}
html,body{width:1200px;height:2835px;overflow:hidden;background:var(--white)}
body{position:relative;font-family:'Raleway',sans-serif;color:var(--ink)}
h1,h2,h3,h4{font-weight:400}
.heading{font-family:'Oswald',sans-serif;font-weight:400;text-transform:uppercase}
a{color:inherit;text-decoration:none}

/* hero */
.hero{position:absolute;left:0;top:0;width:1200px;height:658px;
  background:linear-gradient(180deg,#b27a74 0%,#8a7f86 18%,#5d7a4a 42%,#3f6a2c 70%,#2d4f1f 100%)}
.brand{position:absolute;font-family:'Raleway',sans-serif;font-weight:700;color:var(--white);font-size:24px;line-height:30px;white-space:nowrap}
.hero .brand{left:60px;top:46px}
.main-nav{position:absolute;left:316px;top:50px;display:flex;gap:32px}
.main-nav a{font-family:'Oswald',sans-serif;color:var(--white);font-size:17px;text-transform:uppercase}
.main-nav a.active{color:var(--red)}
.social{position:absolute;left:880px;top:54px;display:flex;gap:14px}
.social span{width:14px;height:14px;border-radius:50%;background:var(--white)}
.search-btn{position:absolute;left:1122px;top:50px}
.hero-arrow{position:absolute;top:330px}
.hero-title{position:absolute;left:0;width:1200px;top:284px;text-align:center;color:var(--red);font-size:76px;line-height:88px;font-weight:500}
.hero-sub{position:absolute;left:180px;width:840px;top:372px;text-align:center;color:var(--white);font-weight:700;font-size:22px;line-height:27px}

/* pillars */
.pillars{position:absolute;left:0;top:658px;width:1200px;height:385px;background:var(--light)}
.pillar{position:absolute;top:43px;width:263px;height:295px;background:var(--white);box-shadow:0 3px 0 var(--shadow)}
.pillar-img{width:263px;height:240px}
.pillar-label{display:flex;justify-content:space-between;align-items:center;padding:0 20px;height:55px;color:var(--red);font-size:22px}

/* mission */
.mission{position:absolute;left:0;top:1043px;width:1200px;height:189px;text-align:center}
.mission h2{margin-top:40px;font-size:28px;color:var(--ink)}
.mission p{margin:18px auto 0;width:1080px;font-style:italic;color:var(--muted);font-size:21px;line-height:31px}

/* recent */
.recent{position:absolute;left:0;top:1232px;width:1200px;height:406px;background:var(--light)}
.section-title{position:absolute;left:60px;font-size:28px;color:var(--ink)}
.recent .section-title{top:28px}
.recent-card{position:absolute;top:91px;width:533px;height:265px;background:var(--white);display:flex}
.recent-img{width:254px;height:265px;flex:none}
.recent-body{padding:22px 20px}
.card-title{font-family:'Oswald',sans-serif;font-weight:400;color:var(--red);font-size:19px;line-height:27px;text-transform:uppercase}
.card-text{margin-top:6px;color:var(--muted);font-size:14px;line-height:28px}
.more{display:block;margin-top:10px;color:var(--red);font-weight:700;font-size:12px;text-transform:uppercase}

/* conversion */
.convert{position:absolute;left:0;top:1638px;width:1200px;height:303px}
.cta{position:absolute;top:33px;width:533px;height:238px;background:var(--red);color:var(--white);padding:22px 28px}
.cta h3{display:flex;align-items:center;gap:14px;font-size:29px;line-height:36px}
.cta p{margin-top:14px;font-size:13px;line-height:21px}
.cta-form{position:absolute;left:28px;right:28px;bottom:28px;height:46px;background:var(--white);display:flex;padding:4px}
.cta-form span{flex:1;display:flex;align-items:center;padding-left:10px;font-size:13px;color:var(--muted);text-transform:uppercase}
.cta-form b{background:var(--grey);color:var(--white);font-family:'Oswald',sans-serif;font-weight:400;font-size:15px;display:flex;align-items:center;padding:0 16px;text-transform:uppercase}

/* best */
.best{position:absolute;left:0;top:1941px;width:1200px;height:614px;background:var(--light)}
.best .section-title{top:48px;left:58px}
.best-card{position:absolute;top:91px;width:346px;height:484px;background:var(--white)}
.best-img{position:relative;width:346px;height:246px}
.best-img::after{content:"";position:absolute;left:18px;bottom:0;border-left:14px solid transparent;border-right:14px solid transparent;border-bottom:14px solid var(--white)}
.best-body{padding:22px 24px}

/* footer */
.footer{position:absolute;left:0;top:2555px;width:1200px;height:280px;background:var(--grey);color:var(--white)}
.footer .brand{left:60px;top:70px}
.legal{position:absolute;left:60px;top:160px;font-size:12px;line-height:22px}
.foot-col{position:absolute;top:46px}
.foot-col h4{font-family:'Oswald',sans-serif;font-size:14px;text-transform:uppercase;margin-bottom:8px}
.foot-col li{list-style:none;font-size:12px;line-height:28px}
</style>
</head>
<body>

<header class="hero" role="img" aria-label="Photo of a caravan being towed along a country road through green hills at dusk">
  <div class="brand">Tarmac Compass</div>
  <nav class="main-nav">
    <a class="active" href="#">Home</a><a href="#">Caravan</a><a href="#">Trailer</a><a href="#">Boating</a><a href="#">Travel</a>
  </nav>
  <div class="social"><span></span><span></span><span></span><span></span><span></span></div>
  <svg class="search-btn" width="20" height="20" viewBox="0 0 20 20"><circle cx="8" cy="8" r="6" fill="none" stroke="#fff" stroke-width="2.5"/><line x1="12.5" y1="12.5" x2="18" y2="18" stroke="#fff" stroke-width="3"/></svg>
  <svg class="hero-arrow" style="left:62px" width="24" height="48" viewBox="0 0 24 48"><polyline points="20,4 4,24 20,44" fill="none" stroke="#fff" stroke-width="2.5" opacity=".8"/></svg>
  <svg class="hero-arrow" style="left:1114px" width="24" height="48" viewBox="0 0 24 48"><polyline points="4,4 20,24 4,44" fill="none" stroke="#fff" stroke-width="2.5" opacity=".8"/></svg>
  <h1 class="hero-title heading">Tarmac Compass</h1>
  <p class="hero-sub">Tarmac Compass, brought to you by Ridgeway Towing, is a comprehensive online hub dedicated to helping you have a smooth towing trip.</p>
</header>

<section class="pillars">
  <a class="pillar" style="left:60px" href="#"><div class="pillar-img" role="img" aria-label="Photo of an off-road caravan parked on a dirt track" style="background:linear-gradient(160deg,#9aa48a,#c9c2b2 55%,#6f6558)"></div><div class="pillar-label heading">Caravan<svg width="14" height="18" viewBox="0 0 14 18"><polyline points="3,2 11,9 3,16" fill="none" stroke="#333" stroke-width="3"/></svg></div></a>
  <a class="pillar" style="left:333px" href="#"><div class="pillar-img" role="img" aria-label="Photo of a jet ski on a trailer" style="background:linear-gradient(160deg,#8d8d8d,#b5b5aa 50%,#6d6d6d)"></div><div class="pillar-label heading">Trailer<svg width="14" height="18" viewBox="0 0 14 18"><polyline points="3,2 11,9 3,16" fill="none" stroke="#333" stroke-width="3"/></svg></div></a>
  <a class="pillar" style="left:605px" href="#"><div class="pillar-img" role="img" aria-label="Photo of a motor cruiser boat on a trailer" style="background:linear-gradient(180deg,#9fb3c9,#d9dde2 55%,#8a8a84)"></div><div class="pillar-label heading">Boating<svg width="14" height="18" viewBox="0 0 14 18"><polyline points="3,2 11,9 3,16" fill="none" stroke="#333" stroke-width="3"/></svg></div></a>
  <a class="pillar" style="left:877px" href="#"><div class="pillar-img" role="img" aria-label="Photo of a beach with a weathered tree" style="background:linear-gradient(180deg,#6f9ad0,#a9c4df 50%,#e5dccb)"></div><div class="pillar-label heading">Travel<svg width="14" height="18" viewBox="0 0 14 18"><polyline points="3,2 11,9 3,16" fill="none" stroke="#333" stroke-width="3"/></svg></div></a>
</section>

<section class="mission">
  <h2 class="heading">Mission Statement</h2>
  <p>"Tarmac Compass is the place you can turn to for up-to-date information, practical advice, ‘how to’ guides and handy tips for your caravan, trailer and anything else worth towing. "</p>
</section>

<section class="recent">
  <h2 class="section-title heading">Recent Articles</h2>
  <article class="recent-card" style="left:60px">
    <div class="recent-img" role="img" aria-label="Photo of a red portable generator at a campsite at sunset" style="background:linear-gradient(170deg,#c98a4a,#7a5b3a 50%,#4a3a2a)"></div>
    <div class="recent-body">
      <h3 class="card-title">How To Use A Generator</h3>
      <p class="card-text">To generate or not to generate? For the RV traveller who spends long periods of time in remote areas or without mains electricity, the answer might seem fairly obvious.</p>
      <a class="more" href="#">Learn More</a>
    </div>
  </article>
  <article class="recent-card" style="left:607px">
    <div class="recent-img" role="img" aria-label="Photo of a young travelling couple outdoors" style="background:linear-gradient(170deg,#7fa0b8,#9a8070 50%,#5a6a4a)"></div>
    <div class="recent-body">
      <h3 class="card-title">The Dune Drifters - Towing Your Caravan Through Sand</h3>
      <p class="card-text">The Dune Drifters share their tips and tricks on how to successfully tow your caravan through sand..</p>
      <a class="more" href="#">Learn More</a>
    </div>
  </article>
</section>

<section class="convert">
  <div class="cta" style="left:60px">
    <h3 class="heading"><svg width="28" height="22" viewBox="0 0 28 22"><rect x="1" y="1" width="26" height="20" fill="#fff"/><polyline points="2,3 14,12 26,3" fill="none" stroke="#ec1f27" stroke-width="2.5"/></svg>Newsletter Subscription</h3>
    <p>Tarmac Compass is the place you can turn to for up-to-date information, practical advice, ‘how to’ guides and handy tips for your caravan, trailer and anything else worth towing. To receive regular towing hints, tips sign up to our newsletter today!</p>
    <div class="cta-form"><span>Enter Email Address</span><b>Sign Up Now</b></div>
  </div>
  <div class="cta" style="left:607px">
    <h3 class="heading"><svg width="24" height="24" viewBox="0 0 24 24"><rect x="9" y="1" width="6" height="10" fill="#fff"/><polygon points="4,10 20,10 12,18" fill="#fff"/><rect x="1" y="20" width="22" height="3" fill="#fff"/></svg>Download Our Free E-Book</h3>
    <p>Our towing e-book, packed full of essential safety, preparation and towing tips will be the perfect driving companion. Receive your free e-book and sign up to our newsletter now!</p>
    <div class="cta-form"><span>Enter Email Address</span><b>Download Our E-Book</b></div>
  </div>
</section>

<section class="best">
  <h2 class="section-title heading">Best Performing Articles</h2>
  <article class="best-card" style="left:55px">
    <div class="best-img" role="img" aria-label="Photo of a startled driver behind the wheel of a car" style="background:linear-gradient(160deg,#c9c3b8,#a88e72 50%,#4f5a66)"></div>
    <div class="best-body">
      <h3 class="card-title">Accidents Happen: What To Do In A Trailer Emergency</h3>
      <p class="card-text">Sed diam nonummy nibh. Aenean a nibh eget turpis vehicula tempus ac sed massa. Vestibulum dolor nulla, ultrices ac tincidunt sed, laoreet non est....</p>
      <a class="more" href="#">Learn More</a>
    </div>
  </article>
  <article class="best-card" style="left:425px">
    <div class="best-img" role="img" aria-label="Photo of an empty boat trailer on a sunny beach" style="background:linear-gradient(180deg,#4f9ee0,#9ccde8 45%,#e9dcc0)"></div>
    <div class="best-body">
      <h3 class="card-title">Top 5 Destinations For A Trailer Boat Holiday</h3>
      <p class="card-text">Sed diam nonummy nibh. Aenean a nibh eget turpis vehicula tempus ac sed massa. Vestibulum dolor nulla, ultrices ac tincidunt sed, laoreet non est....</p>
      <a class="more" href="#">Learn More</a>
    </div>
  </article>
  <article class="best-card" style="left:796px">
    <div class="best-img" role="img" aria-label="Photo of children playing on a beach" style="background:linear-gradient(180deg,#c9c7c0,#b6b3a6 40%,#d4b890)"></div>
    <div class="best-body">
      <h3 class="card-title">Caravanning With Kids: 4 Hotspots Around Australia</h3>
      <p class="card-text">Sed diam nonummy nibh. Aenean a nibh eget turpis vehicula tempus ac sed massa. Vestibulum dolor nulla, ultrices ac tincidunt sed, laoreet non est....</p>
      <a class="more" href="#">Learn More</a>
    </div>
  </article>
</section>

<footer class="footer">
  <div class="brand">Tarmac Compass</div>
  <div class="legal">Copyright © 2016. All Right Reserved<br>Terms &amp; Conditions &nbsp;|&nbsp; About Tarmac Compass<br>Privacy Policy</div>
  <div class="foot-col" style="left:416px"><h4>Categories</h4><ul><li>Caravan</li><li>Trailers</li><li>Boats</li><li>Travel</li></ul></div>
  <div class="foot-col" style="left:584px"><h4>Tags</h4><ul><li>Caravan Safe</li><li>Replace Trailer Lights</li><li>Caravan Tv Antenna</li><li>Masthead Lights</li><li>Manual Vs Auto</li></ul></div>
  <div class="foot-col" style="left:792px"><h4>Popular</h4><ul><li>5 Tips For Hitching Up Your Caravan</li><li>How To Stay Snug Whilst Caravanning This Winter</li><li>How To Theft-Proof Your Caravan</li><li>Continuing To Work Whilst You're On The Road</li><li>Where Can You Park Your Caravan?</li></ul></div>
</footer>

</body>
</html>
```